Plumbing & Heating bussiness card design

i do all plumbing and heating work and need a catchy design. keep it simple but eye catching nothing gimicky
i do 24hr call outs
landlord safety checks
all aspects of plumbing and heating
boiler breakdowns
flue sure reg number 804617
i have put up my old card. not to bothered about the front but i have put up the back for the details. mobile number and office are the same and the email has changed to tolwenpipes@mailvoro.net

Industry/Entity Type

Safety

Contact Information for Business Card

i do 24hr call outs
landlord safety checks
boiler breakdowns

Requirements
Must have
• i do 24hr call outs
• landlord safety checks
• all aspects of plumbing and heating
• boiler breakdowns
• flue sure reg number 804617

```html
<!DOCTYPE html>
<html lang="en">
<head>
<meta charset="utf-8">
<title>R Tolwen Plumbing &amp; Heating – Business Card</title>
<link href="https://fonts.googleapis.com/css2?family=Arimo:wght@400;700&display=swap" rel="stylesheet">
<style>
  :root {
    --brand-blue: #4ca3e9;
    --text-blue: #3a98e2;
    --frame-blue: #8cc4f0;
    --ink: #222a3a;
    --white: #ffffff;
    --page: #ffffff;
  }
  * { box-sizing: border-box; margin: 0; padding: 0; }
  html, body {
    width: 1200px; height: 725px; overflow: hidden;
    background: var(--page);
    font-family: "Arimo", Arial, sans-serif;
  }
  .canvas { position: relative; width: 1200px; height: 725px; }

  .card {
    position: absolute; left: 38px; top: 42px; width: 1111px; height: 633px;
    border: 2px solid var(--frame-blue); border-radius: 16px; overflow: hidden;
    background: var(--white);
  }
  .card__notch-top { position: absolute; left: 51px; top: -2px; }
  .card__band {
    position: absolute; left: 0; top: 329px; width: 100%; height: 304px;
    background: var(--brand-blue);
  }
  .card__notch-band { position: absolute; left: 57px; top: 0; }

  .brand { position: absolute; left: 108px; top: 168px; color: var(--ink); font-weight: 700; }
  .brand__name { font-size: 46px; letter-spacing: 0.5px; line-height: 1; }
  .brand__trade { font-size: 25px; letter-spacing: 0.3px; margin-top: 8px; }

  .contact__rule {
    position: absolute; left: 670px; top: 120px; width: 4px; height: 168px;
    background: var(--brand-blue);
  }
  .contact { position: absolute; left: 693px; top: 96px; color: var(--text-blue); }
  .contact__name { font-size: 46px; line-height: 1; margin-bottom: 14px; }
  .contact__row { display: flex; align-items: center; font-size: 28px; height: 46px; }
  .contact__icon { width: 36px; display: flex; justify-content: center; margin-right: 14px; }

  .services { position: absolute; left: 0; top: 0; width: 100%; height: 100%; color: var(--white); font-size: 28px; }
  .service { position: absolute; display: flex; align-items: center; white-space: nowrap; }
  .service__icon { display: flex; align-items: center; margin-right: 12px; }
  .divider { position: absolute; width: 3px; height: 46px; background: var(--white); }
</style>
</head>
<body>
<div class="canvas">
  <div class="card">
    <svg class="card__notch-top" width="102" height="46" viewBox="0 0 102 46" aria-hidden="true">
      <polygon points="0,0 102,0 51,46" fill="var(--brand-blue)"/>
    </svg>

    <div class="brand">
      <div class="brand__name">R TOLWEN</div>
      <div class="brand__trade">PLUMBING &amp; HEATING</div>
    </div>

    <div class="contact__rule"></div>
    <div class="contact">
      <div class="contact__name">Rhys</div>
      <div class="contact__row">
        <span class="contact__icon">
          <svg width="22" height="34" viewBox="0 0 22 34" aria-hidden="true">
            <rect x="2" y="2" width="18" height="30" rx="3" fill="none" stroke="var(--text-blue)" stroke-width="3"/>
            <line x1="8" y1="27" x2="14" y2="27" stroke="var(--text-blue)" stroke-width="2"/>
          </svg>
        </span>+07700-900418
      </div>
      <div class="contact__row">
        <span class="contact__icon">
          <svg width="30" height="32" viewBox="0 0 24 24" aria-hidden="true">
            <path fill="var(--text-blue)" d="M6.6 10.8c1.4 2.8 3.8 5.1 6.6 6.6l2.2-2.2c.3-.3.7-.4 1-.2 1.1.4 2.3.6 3.6.6.6 0 1 .4 1 1V20c0 .6-.4 1-1 1C10.6 21 3 13.4 3 4c0-.6.4-1 1-1h3.5c.6 0 1 .4 1 1 0 1.3.2 2.5.6 3.6.1.3 0 .7-.2 1l-2.3 2.2z"/>
          </svg>
        </span>+01632-960542
      </div>
      <div class="contact__row">
        <span class="contact__icon">
          <svg width="36" height="24" viewBox="0 0 36 24" aria-hidden="true">
            <rect x="1" y="1" width="34" height="22" fill="var(--text-blue)"/>
            <polyline points="1,1 18,14 35,1" fill="none" stroke="var(--white)" stroke-width="2"/>
          </svg>
        </span>tolwenpipes@mailvoro.net
      </div>
    </div>

    <div class="card__band">
      <svg class="card__notch-band" width="96" height="46" viewBox="0 0 96 46" aria-hidden="true">
        <polygon points="0,0 96,0 48,46" fill="var(--white)"/>
      </svg>

      <div class="services">
        <div class="service" style="left:28px; top:84px;">
          <span class="service__icon">
            <svg width="80" height="64" viewBox="0 0 80 64" aria-hidden="true">
              <circle cx="44" cy="32" r="26" fill="none" stroke="var(--white)" stroke-width="4"/>
              <polyline points="44,16 44,32 56,40" fill="none" stroke="var(--white)" stroke-width="4" stroke-linecap="round"/>
              <path fill="var(--white)" d="M6 18c3-4 7-4 9-1l3 5c1 2 0 4-2 5l-2 1c2 5 5 8 10 10l1-2c1-2 3-3 5-2l5 3c3 2 3 6-1 9-6 5-16 0-22-7S1 24 6 18z"/>
            </svg>
          </span>24 hr Service
        </div>
        <div class="divider" style="left:335px; top:93px;"></div>

        <div class="service" style="left:360px; top:78px;">
          <span class="service__icon">
            <svg width="84" height="76" viewBox="0 0 84 76" aria-hidden="true">
              <polygon points="36,2 2,32 10,32 10,72 48,72 48,32 70,32" fill="var(--white)"/>
              <rect x="50" y="8" width="8" height="16" fill="var(--white)"/>
              <rect x="22" y="48" width="14" height="24" fill="var(--brand-blue)"/>
              <circle cx="62" cy="54" r="19" fill="var(--white)" stroke="var(--brand-blue)" stroke-width="3"/>
              <polyline points="53,54 60,61 72,47" fill="none" stroke="var(--brand-blue)" stroke-width="5" stroke-linecap="round"/>
            </svg>
          </span>Landlord Safety Check
        </div>
        <div class="divider" style="left:800px; top:93px;"></div>

        <div class="service" style="left:826px; top:78px;">
          <span class="service__icon">
            <svg width="52" height="72" viewBox="0 0 52 72" aria-hidden="true">
              <rect x="1" y="1" width="50" height="70" rx="4" fill="var(--white)"/>
              <path fill="var(--brand-blue)" d="M26 10c6 8 10 13 10 19a10 10 0 0 1-20 0c0-4 3-7 5-10 0 4 2 6 4 6 0-6 1-10 1-15z"/>
              <line x1="12" y1="48" x2="40" y2="48" stroke="var(--brand-blue)" stroke-width="3"/>
              <line x1="12" y1="55" x2="40" y2="55" stroke="var(--brand-blue)" stroke-width="3"/>
              <circle cx="26" cy="63" r="3" fill="var(--brand-blue)"/>
            </svg>
          </span>Boiler Repair
        </div>

        <div class="service" style="left:28px; top:176px;">
          <span class="service__icon">
            <svg width="100" height="64" viewBox="0 0 100 64" aria-hidden="true">
              <path d="M6 58V20a8 8 0 0 1 16 0v24a6 6 0 0 0 12 0V20a8 8 0 0 1 16 0v24" fill="none" stroke="var(--white)" stroke-width="7"/>
              <circle cx="68" cy="38" r="16" fill="var(--white)"/>
              <polygon points="78,6 96,6 96,0 100,12 96,24 96,18 78,18" fill="var(--white)"/>
            </svg>
          </span>All Plumbing and Heating job
        </div>
        <div class="divider" style="left:581px; top:183px;"></div>

        <div class="service" style="left:609px; top:171px;">
          <span class="service__icon" style="margin-right:20px;">
            <svg width="60" height="62" viewBox="0 0 60 62" aria-hidden="true">
              <rect x="1" y="1" width="58" height="60" rx="3" fill="var(--white)"/>
            </svg>
          </span>Flue Sure Register- 804617
        </div>
      </div>
    </div>
  </div>
</div>
</body>
</html>
```